Natural Skincare brand needs new labels!

We are a natural and organic skin care brand based in the united states. We are looking for unique product label designs that will help our brand stand out. We want the labels to look elegant and natural, but also incorporate some color. We want a design aspect like a line drawing on the labels, see examples. Please refer to our website to see our current labels and to get more of a feel of who we are. Our logo is included. We are looking for 5 labels for 5 different Products.
1. Body butter: 1.5"x9" rectangle wrap around 12oz jar with black lid
2. Eczema Salve: 1.5" circle silver metal tin
3. Glow Serum: 1.5"x3" rectangle Blue Dropper Bottle with black top
4. Mineral Mist: 1.5"x3" clear glass sprayer bottle (want clear label)
website: www.venalubotanics.com
Instagram: @venalubotanics

```html
<!DOCTYPE html>
<html lang="en">
<head>
<meta charset="utf-8">
<title>Venalu Label Designs</title>
<link rel="stylesheet" href="https://fonts.googleapis.com/css2?family=Archivo+Black&family=Montserrat:wght@300;400;600&display=swap">
<style>
  :root {
    --kraft: #8f6d46;
    --ink: #1b1b1b;
    --paper: #ffffff;
    --leaf-gold: #f29a12;
    --leaf-brown: #2a2118;
  }
  * { box-sizing: border-box; margin: 0; padding: 0; }
  html, body { width: 1200px; height: 1200px; overflow: hidden; }
  body { background: var(--kraft); font-family: "Montserrat", sans-serif; color: var(--ink); position: relative; }
  .abs { position: absolute; }

  .leaf-art { position: absolute; border-radius: 46% 54% 42% 58% / 55% 40% 60% 45%; }
  .leaf-art.gold { background: linear-gradient(160deg, rgba(242,154,18,.10), rgba(242,154,18,.22) 50%, rgba(242,154,18,.10)); }
  .leaf-art.brown { background: linear-gradient(160deg, rgba(42,33,24,.08), rgba(42,33,24,.18) 50%, rgba(42,33,24,.08)); }

  .brand { display: flex; flex-direction: column; align-items: center; }
  .brand-row { display: flex; align-items: center; gap: 7px; }
  .brand-dot { border-radius: 50%; background: var(--ink); flex: none; }
  .brand-name { font-family: "Montserrat", sans-serif; font-weight: 600; letter-spacing: .06em; line-height: 1; color: var(--ink); white-space: nowrap; }

  .display { font-family: "Archivo Black", sans-serif; text-transform: uppercase; line-height: .88; text-align: center; }
  .rule { border-top: 1.2px solid var(--ink); }

  /* body cream wrap */
  .wrap-band { left: 42px; top: 87px; width: 1114px; height: 210px; background: var(--ink); overflow: hidden; }
  .wrap-tab { left: 323px; top: 0; width: 108px; height: 210px; background: var(--paper); display: flex; align-items: center; justify-content: center; }
  .wrap-tab .display { transform: rotate(-90deg); font-size: 37px; white-space: nowrap; }
  .wrap-face { left: 454px; top: 0; width: 213px; height: 210px; background: var(--paper); display: flex; flex-direction: column; align-items: center; padding-top: 52px; }
  .wrap-face .brand { margin-bottom: 38px; }
  .wrap-face .rule { width: 158px; }
  .wrap-kicker { font-weight: 300; font-size: 11px; line-height: 1.1; margin-top: 6px; color: #555; }
  .wrap-name { font-weight: 400; font-size: 12.5px; line-height: 1.2; margin-bottom: 5px; }
  .wrap-tags { font-size: 6.6px; letter-spacing: .05em; margin-top: 6px; white-space: nowrap; }

  /* eczema tin */
  .tin { left: 280px; top: 339px; width: 448px; height: 448px; border-radius: 50%; background: var(--ink); overflow: hidden; }
  .tin-face { left: 128px; top: 0; width: 191px; height: 284px; background: var(--paper); display: flex; flex-direction: column; align-items: center; padding-top: 116px; }
  .tin-face .brand { margin-bottom: 48px; }
  .tin-face .rule { width: 156px; }
  .tin-face .display { font-size: 23px; margin: 3px 0 2px; }
  .tin-claim { font-size: 14.5px; text-align: center; line-height: 1.22; margin-top: 9px; }
  .tin-ingredients { left: 0; top: 303px; width: 448px; text-align: center; color: var(--paper); }
  .tin-ingredients h3 { font-weight: 400; font-size: 18px; letter-spacing: .03em; margin-bottom: 8px; }
  .tin-ingredients p { font-weight: 300; font-size: 11.6px; letter-spacing: .07em; line-height: 1.55; }

  /* mineral mist clear label */
  .mist { left: 866px; top: 593px; width: 264px; display: flex; flex-direction: column; align-items: center; }
  .mist .display { font-size: 30px; margin-top: 62px; }

  /* glow serum */
  .serum-band { left: 298px; top: 828px; width: 858px; height: 350px; background: var(--ink); }
  .serum-face { left: 309px; top: 1px; width: 241px; height: 293px; background: var(--paper); display: flex; flex-direction: column; align-items: center; padding-top: 82px; }
  .serum-face .brand { margin-bottom: 52px; }
  .serum-face .rule { width: 170px; }
  .serum-face .display { font-size: 27px; margin: 4px 0 2px; }
  .serum-sub { font-size: 14.5px; text-align: center; letter-spacing: .05em; line-height: 1.2; margin-top: 15px; }

  .sheet-title { left: 42px; top: 780px; width: 104px; height: 394px; }
  .sheet-title span { position: absolute; left: 52px; top: 197px; transform: translate(-50%,-50%) rotate(-90deg); font-family: "Archivo Black", sans-serif; font-size: 52px; line-height: 1; white-space: nowrap; text-align: left; color: var(--ink); }
</style>
</head>
<body>

  <section class="abs wrap-band" aria-label="Body cream jar wrap">
    <div class="leaf-art gold" style="left:216px;top:5px;width:108px;height:186px" role="img" aria-label="Gold line-drawn leafy branch"></div>
    <div class="leaf-art gold" style="left:889px;top:0;width:225px;height:210px" role="img" aria-label="Gold line-drawn leafy branch"></div>
    <div class="abs wrap-tab"><div class="display">Body<br>Cream</div></div>
    <div class="abs wrap-face">
      <div class="brand">
        <div class="brand-row"><span class="brand-dot" style="width:13px;height:13px"></span><span class="brand-name" style="font-size:21px">VENALU SKIN</span></div>
      </div>
      <div class="rule"></div>
      <div class="wrap-kicker">UNSCENTED</div>
      <div class="wrap-name">NATURAL BODY CREAM</div>
      <div class="rule"></div>
      <div class="wrap-tags">MOISTURISING | NOURISHING | SENSITIVE | DRY SKIN</div>
    </div>
  </section>

  <section class="abs tin" aria-label="Eczema salve tin lid">
    <div class="leaf-art gold" style="left:34px;top:99px;width:96px;height:223px" role="img" aria-label="Gold line-drawn leafy branch"></div>
    <div class="leaf-art gold" style="left:316px;top:58px;width:84px;height:174px" role="img" aria-label="Gold line-drawn leafy branch"></div>
    <div class="abs tin-face">
      <div class="brand">
        <div class="brand-row"><span class="brand-dot" style="width:12px;height:12px"></span><span class="brand-name" style="font-size:19px">VENALU SKIN</span></div>
      </div>
      <div class="rule"></div>
      <div class="display">Eczema<br>Salve</div>
      <div class="rule"></div>
      <div class="tin-claim">HEALING &amp;<br>REGENERATING</div>
    </div>
    <div class="abs tin-ingredients">
      <h3>INGREDIENTS:</h3>
      <p>Organic Sesame Oil • Organic Calendula Flower<br>Organic Licorice Root • Organic Plantain Leaf<br>Organic Vitamin E Oil • Organic Beezwax</p>
    </div>
  </section>

  <div class="leaf-art brown" style="left:823px;top:338px;width:270px;height:244px" role="img" aria-label="Dark line-drawn leafy branch"></div>

  <section class="abs mist" aria-label="Mineral mist clear label">
    <div class="brand" style="margin-top:50px">
      <div class="brand-row"><span class="brand-dot" style="width:20px;height:20px"></span><span class="brand-name" style="font-size:30px">VENALU SKIN</span></div>
    </div>
    <div class="display">Mineral<br>Mist</div>
  </section>

  <section class="abs serum-band" aria-label="Glow serum bottle label">
    <div class="leaf-art gold" style="left:168px;top:10px;width:143px;height:168px" role="img" aria-label="Gold line-drawn leafy branch"></div>
    <div class="leaf-art gold" style="left:550px;top:159px;width:115px;height:174px" role="img" aria-label="Gold line-drawn leafy branch"></div>
    <div class="abs serum-face">
      <div class="brand">
        <div class="brand-row"><span class="brand-dot" style="width:15px;height:15px"></span><span class="brand-name" style="font-size:24px">VENALU SKIN</span></div>
      </div>
      <div class="rule"></div>
      <div class="display">Glow<br>Serum</div>
      <div class="rule"></div>
      <div class="serum-sub">Manjishta + Safflower<br>Glow + Even Skin Toner</div>
    </div>
  </section>

  <h1 class="abs sheet-title"><span>Venalu<br>Label Designs</span></h1>

</body>
</html>
```